Flyer Design - Child Care Centre

I need a flyer design (d/sided), full colour for a Child Care Centre that I have recently bought. Check out my website (tiny-sprouts.com.au) for information on what we do, our services, philosophy, fees and hours of operation.

The purpose of this flyer is to advertise our services as a child care centre (under new management) to the local community and with various hospitals.

The flyer should embody our philosophy, the text on my home page (particularly our QX focus) and some of the parent testimonials. It should also include my logo and Zibb (refer attached AI and jpeg files, eps available on request).

Feel free to add stock photo's of kids and cartoon characters and use the following CMYK colours if incorporating any coloured text. Green: C-78, M-0, Y-100, K-0 Magenta: C-0, M-100, Y-33, K-10

```html
<!DOCTYPE html>
<html lang="en">
<head>
<meta charset="utf-8">
<title>Tiny Sprouts – Double-sided Flyer</title>
<link rel="stylesheet" href="https://fonts.googleapis.com/css2?family=Arimo:wght@400;700&family=Teko:wght@500;600&family=Yanone+Kaffeesatz:wght@400;500;600&family=Archivo+Black&display=swap">
<style>
:root{
  --ink:#111;
  --rule-blue:#2b45e0;
  --green:#3fd12a;
  --purple:#9b34d6;
  --magenta:#c31e5e;
  --red:#e3231e;
  --blue:#1a56d6;
  --text-blue:#2741b8;
  --sky:#2aa8e8;
  --footer-top:#3b93f2;
  --footer-bottom:#1466d8;
  --frame:#f2a7b3;
  --paper:#ffffff;
}
*{margin:0;padding:0;box-sizing:border-box}
html,body{width:1200px;height:900px;overflow:hidden;background:var(--paper)}
.sheet{position:relative;width:1200px;height:900px;font-family:"Arimo",Arial,sans-serif;color:var(--ink)}
.side-label{position:absolute;top:14px;font-family:"Archivo Black",Arial,sans-serif;font-size:22px;letter-spacing:34px}
.side-label.back{left:192px}
.side-label.front{left:795px}
.guide-h{position:absolute;left:0;top:46px;width:1200px;height:3px;background:var(--rule-blue)}
.guide-b{position:absolute;left:0;top:888px;width:1200px;height:4px;background:var(--rule-blue)}
.guide-v{position:absolute;left:598px;top:0;width:3px;height:892px;background:var(--rule-blue)}
.panel{position:absolute;top:49px;width:595px;height:839px;overflow:hidden;
  background:linear-gradient(135deg,#eef0f4 0%,#fff 30%,#e9ecf1 55%,#fff 80%,#e4e7ec 100%)}
.panel.back{left:0}
.panel.front{left:603px;width:597px}
.frame{position:absolute;border:1px solid var(--frame)}
.abs{position:absolute}
.placeholder{position:absolute}
.photo-circle{position:absolute;border-radius:50%}
.brand-name{position:absolute;font-family:"Teko",sans-serif;font-weight:600;color:var(--purple);text-align:center;line-height:1}
.brand-sub{position:absolute;font-family:"Arimo",Arial,sans-serif;font-weight:700;color:var(--green);text-align:center}
.badge{position:absolute;border-radius:40px;background:linear-gradient(180deg,#7fd6ff,#1aa0e6);color:#fff;
  font-family:"Yanone Kaffeesatz",sans-serif;font-weight:500;text-align:center;line-height:.95;
  box-shadow:0 3px 0 #0c6fb3}
.section-head{position:absolute;left:0;width:595px;text-align:center;font-weight:700;color:var(--purple);letter-spacing:5px;font-size:17px}
.copy{position:absolute;left:0;width:595px;text-align:center;font-size:12.5px;line-height:13.2px;color:var(--text-blue)}
.fees{position:absolute;left:0;width:595px;text-align:center;font-size:13px;line-height:13.4px;color:var(--purple)}
.fees .lead{color:var(--red)}
.note{position:absolute;left:0;width:595px;text-align:center;font-size:11.5px;line-height:12px;color:var(--red)}
.rule{position:absolute;height:1px;background:var(--red)}
.address{position:absolute;font-family:"Yanone Kaffeesatz",sans-serif;font-weight:600;font-size:27px;white-space:nowrap}
.address .r{color:var(--red)} .address .b{color:var(--blue)}
.footer{position:absolute;left:0;bottom:0;width:100%;height:101px;
  background:linear-gradient(180deg,var(--footer-top),var(--footer-bottom));color:#fff;
  font-family:"Yanone Kaffeesatz",sans-serif}
.footer .line1{position:absolute;left:40px;top:8px;font-family:"Arimo",Arial,sans-serif;font-weight:700;font-size:13px;white-space:nowrap}
.footer .sq{display:inline-block;width:11px;height:11px;background:#fff;margin:0 4px 0 8px;vertical-align:-1px}
.footer .hours{position:absolute;left:32px;top:27px;font-size:21px;line-height:19px;text-align:right;width:270px}
.footer .contact{position:absolute;left:305px;top:27px;font-size:21px;line-height:19px;padding-left:8px;border-left:2px dotted #fff}
.footer .box{position:absolute;left:104px;top:48px;width:432px;height:23px;border:1px solid #fff;border-top:none}
.headline{position:absolute;right:282px;top:375px;width:320px;text-align:right;font-family:"Yanone Kaffeesatz",sans-serif;font-weight:500;font-size:33px;line-height:30.5px}
.headline .r{color:var(--red)} .headline .b{color:var(--blue)}
.activities{position:absolute;left:0;top:599px;width:315px;height:62px;background:var(--red);color:#fff;text-align:right;font-family:"Yanone Kaffeesatz",sans-serif;padding-right:14px}
.activities .spaced{font-size:24px;letter-spacing:13px;line-height:26px;padding-top:3px}
.activities .big{font-size:31px;font-weight:600;line-height:30px}
.encourage{position:absolute;right:296px;top:661px;text-align:right;font-family:"Yanone Kaffeesatz",sans-serif;font-size:24px;line-height:22.5px;color:var(--blue)}
.map-card{position:absolute;left:322px;top:456px;width:252px;height:277px;border:1px solid var(--frame);background:#fff}
.map-card .addr{position:absolute;left:0;top:8px;width:100%;text-align:center;font-family:"Yanone Kaffeesatz",sans-serif;font-weight:600;font-size:19px;line-height:17px;color:var(--red)}
</style>
</head>
<body>
<div class="sheet">
  <div class="side-label back">BACK</div>
  <div class="side-label front">FRONT</div>

  <!-- BACK SIDE -->
  <section class="panel back">
    <div class="frame" style="left:18px;top:25px;width:556px;height:700px"></div>
    <div class="frame" style="left:38px;top:402px;width:530px;height:152px;border-color:var(--frame)"></div>

    <div class="placeholder" role="img" aria-label="Mascot illustration: cartoon character with spiky purple hair reading a book"
      style="left:238px;top:40px;width:108px;height:122px;border-radius:40px 40px 20px 20px;background:radial-gradient(circle at 50% 35%,#c98cf0,#8a2ed0 60%,#5a1fa0)"></div>

    <div class="brand-name" style="left:100px;top:172px;width:395px;font-size:56px">Tiny Sprouts</div>
    <div class="brand-sub" style="left:100px;top:217px;width:395px;font-size:14px">Early Development &amp; Education Centre</div>

    <div class="badge" style="left:428px;top:120px;width:135px;height:44px;font-size:19px;padding-top:3px;transform:rotate(10deg)">UNDER NEW<br>MANAGEMENT</div>

    <div class="photo-circle" role="img" aria-label="Photo of a boy writing at a desk" style="left:15px;top:174px;width:98px;height:98px;background:radial-gradient(circle,#e8c6a8,#6f8fb0)"></div>
    <div class="photo-circle" role="img" aria-label="Photo of a girl painting" style="left:15px;top:262px;width:104px;height:104px;background:radial-gradient(circle,#f0c9ad,#b7705a)"></div>
    <div class="photo-circle" role="img" aria-label="Photo of a smiling toddler" style="left:468px;top:174px;width:100px;height:100px;background:radial-gradient(circle,#f3d4b8,#a36a3c)"></div>
    <div class="photo-circle" role="img" aria-label="Photo of a child in a red jumper" style="left:468px;top:264px;width:100px;height:100px;background:radial-gradient(circle,#f1cdb0,#c8342a)"></div>

    <div class="section-head" style="top:250px">OUR PHILOSPHY</div>
    <div class="copy" style="top:270px">Every child is unique and we believe that success<br>and growth comes from learning with encouragement<br>and praise.<br>Our teachers focus on building every child's self esteem<br>and confidence through positive feedback,<br>We nurture their natural strengths.<br><br>A child sees the world around them with wonder and awe,<br>we believe in encouraging their natural curiosity.</div>

    <div class="section-head" style="top:393px">OUR GOALS</div>
    <div class="copy" style="top:410px">We act as an extension of the home. We strive to provide<br>an environment where children feel loved,<br>accepted and secure.&nbsp; We foster strong partnerships with home,<br>creating a smooth and caring transition between the home and the Centre.<br>Parents participation is encouraged and educators work in consultation with parents.<br><br>Children are encouraged to achieve their best socially, emotionally<br>and academically. We listen<br>to their voices.&nbsp; We recognise our moral and social obligation to our children,<br>their families and the greater community providing the children with a<br>core foundation that will support them through<br>life towards becoming active members of the community.</div>

    <div class="section-head" style="top:563px">OUR FEES</div>
    <div class="fees" style="top:582px"><span class="lead">Fees are payable two weeks in advance via direct debit.</span><br>BABIES (0-2YRS)&nbsp; :&nbsp; $85.00 PER DAY<br>TODDLERS (2-3YRS)&nbsp;&nbsp; :&nbsp; $85.00 PER DAY<br>KINDY (3-6YRS)&nbsp; :&nbsp; $85.00 PER DAY<br>BEFORE SCHOOL&nbsp; :&nbsp; $25.00 PER DAY<br>AFTER SCHOOL&nbsp; :&nbsp; $28.00 PER DAY<br>*VACATION CARE&nbsp; :&nbsp; $85.00 PER DAY</div>
    <div class="rule" style="left:28px;top:677px;width:540px"></div>
    <div class="note" style="top:679px">*Please note that Vacation Care does not include excursions. We create a vacation care plan<br>to be affordable&nbsp; e.g. only 2 paying excursions per week.</div>
    <div class="rule" style="left:28px;top:703px;width:540px"></div>

    <div class="address" style="left:30px;top:704px"><span class="r">57 Banksia Road,</span> <span class="b">Willow Creek,</span> <span class="r">Western Australia 6999</span></div>

    <footer class="footer">
      <div class="line1">T:&nbsp; +61 (08) 5550 1234&nbsp; /<span class="sq"></span>TINYSPROUTSOZ&nbsp;<span class="sq"></span>@TINYSPROUTSOZ</div>
      <div class="hours">Open Monday - Friday 6:00am - 6:00p<br>(except public holidays):</div>
      <div class="contact">E: enquiries@tiny-sprouts.com.au<br>W: www.tiny-sprouts.com.au</div>
      <div class="box"></div>
    </footer>
  </section>

  <!-- FRONT SIDE -->
  <section class="panel front">
    <div class="frame" style="left:24px;top:25px;width:552px;height:700px"></div>

    <div class="placeholder" role="img" aria-label="Mascot illustration: cartoon character with spiky purple hair reading a book"
      style="left:228px;top:36px;width:130px;height:150px;border-radius:48px 48px 24px 24px;background:radial-gradient(circle at 50% 35%,#c98cf0,#8a2ed0 60%,#5a1fa0)"></div>

    <div class="brand-name" style="left:100px;top:184px;width:400px;font-size:70px">Tiny Sprouts</div>
    <div class="brand-sub" style="left:100px;top:245px;width:400px;font-size:17px">Early Development &amp; Education Centre</div>

    <div class="badge" style="left:20px;top:282px;width:270px;height:66px;border-radius:50px;font-size:33px;padding-top:2px;transform:rotate(8deg)">UNDER NEW<br>MANAGEMENT</div>

    <div class="photo-circle" role="img" aria-label="Photo of smiling children lying together" style="left:342px;top:276px;width:138px;height:138px;border:6px solid var(--red);background:radial-gradient(circle,#f4cdae,#7fb04a 70%,#e2a13a)"></div>
    <div class="photo-circle" role="img" aria-label="Photo of a boy reading at a table" style="left:458px;top:316px;width:92px;height:92px;border:5px solid var(--red);background:radial-gradient(circle,#f1c8a6,#c9523a)"></div>

    <div class="headline"><span class="r">Tiny Sprouts</span> <span class="b">provides</span><br><span class="b">an inclusive</span><br><span class="b">and</span> <span class="r">Open Program</span><br><span class="b">where all children</span><br><span class="b">are considered</span> <span class="r">Unique</span><br><span class="r">individuals and</span><br><span class="r">Diversity</span> <span class="b">is Valued</span></div>

    <div class="activities"><div class="spaced">We provide</div><div class="big">A VARIETY OF ACTIVITIES</div></div>
    <div class="encourage">that encourages the<br>participation<br>of all children</div>

    <div class="map-card">
      <div class="addr">57 Banksia Road, Willow Creek,<br>Western Australia 6999</div>
      <div class="placeholder" role="img" aria-label="Street map showing the centre's location" style="left:7px;top:50px;width:238px;height:220px;background:linear-gradient(135deg,#eceae4,#e2e6dc 50%,#dfe8d4)"></div>
    </div>

    <footer class="footer">
      <div class="line1">T:&nbsp; +61 (08) 5550 1234&nbsp; /<span class="sq"></span>TINYSPROUTSOZ&nbsp;<span class="sq"></span>@TINYSPROUTSOZ</div>
      <div class="hours">Open Monday - Friday 6:00am - 6:00p<br>(except public holidays):</div>
      <div class="contact">E: enquiries@tiny-sprouts.com.au<br>W: www.tiny-sprouts.com.au</div>
      <div class="box"></div>
    </footer>
  </section>

  <div class="guide-h"></div>
  <div class="guide-b"></div>
  <div class="guide-v"></div>
</div>
</body>
</html>
```